Business Card Design

Contact Information for Business Card

A vertical business card request- a medium & light gray with silverpine tree logo (logo is attached)

Please use Trebuchet font -- if possible- can we use two different color gray? (See pictures attached below)
Info on the front should be the Silverpine tree logo - on the top of the card, followed by the info ...
Card to read: " " indicated what should be on the card --
Name: " Carla Merrow "
Title : "Partner "
" Office: 202.555.0147 "
" Mobile: 202.555.0183 "

Backside of the card - solid medium color gray color w/ address and small message centered in the card - Trebuchet font
to read:

" 718 B North Larkmoor Avenue, NE "
" Washington, DC 20019 "

Then below address to read:
" Fundraising | Event Planning | Political Consulting "

```html
<!DOCTYPE html>
<html lang="en">
<head>
<meta charset="utf-8">
<title>Silverpine Strategies – Business Cards</title>
<link href="https://fonts.googleapis.com/css2?family=PT+Sans:wght@400;700&family=Roboto+Condensed:wght@400&display=swap" rel="stylesheet">
<style>
  :root {
    --backdrop: #cbcbcb;
    --gray-medium: #6f6e6c;
    --gray-light: #f3f3f3;
    --ink-white: #ffffff;
    --ink-gray: #6a6a6a;
    --card-shadow: rgba(0, 0, 0, 0.28);
  }
  * { margin: 0; padding: 0; box-sizing: border-box; }
  html, body {
    width: 1200px;
    height: 1005px;
    overflow: hidden;
    background: var(--backdrop);
    font-family: "PT Sans", "Trebuchet MS", sans-serif;
  }
  .canvas {
    position: relative;
    width: 1200px;
    height: 1005px;
  }
  .card {
    position: absolute;
    top: 205px;
    width: 340px;
    height: 595px;
    background: var(--gray-medium);
    box-shadow: 6px 8px 14px var(--card-shadow);
    overflow: hidden;
  }
  .card--back { left: 235px; }
  .card--front { left: 625px; }

  .brand {
    position: absolute;
    left: 0;
    right: 0;
    text-align: center;
    color: var(--ink-white);
    font-weight: 400;
  }
  .brand__name {
    display: block;
    font-size: 33px;
    letter-spacing: 1px;
    line-height: 1;
    text-transform: uppercase;
  }
  .brand__sub {
    display: block;
    font-size: 17px;
    letter-spacing: 2px;
    line-height: 1.4;
    text-transform: uppercase;
    text-align: right;
    padding-right: 44px;
  }
  .brand__mark {
    display: block;
    width: 14px;
    height: 14px;
    margin: 0 auto 14px;
    border-radius: 50%;
    background: var(--ink-white);
  }
  .card--back .brand { top: 225px; }
  .card--front .brand { top: 212px; }

  .address {
    position: absolute;
    left: 0;
    right: 0;
    top: 455px;
    text-align: center;
    color: var(--ink-white);
    font-size: 15.5px;
    line-height: 1.45;
  }
  .services {
    position: absolute;
    left: 0;
    right: 0;
    top: 528px;
    text-align: center;
    color: var(--ink-white);
    font-family: "Roboto Condensed", "Arial Narrow", sans-serif;
    font-size: 14px;
  }
  .services__sep { padding: 0 5px; }

  .card__panel {
    position: absolute;
    left: 0;
    right: 0;
    top: 330px;
    bottom: 0;
    background: var(--gray-light);
    padding: 36px 0 0 36px;
    color: var(--ink-gray);
  }
  .person__name { font-size: 21px; line-height: 1.2; }
  .person__title { font-size: 14px; margin-top: 4px; margin-left: 4px; }
  .contact {
    list-style: none;
    margin-top: 26px;
    margin-left: 4px;
  }
  .contact__item {
    display: flex;
    align-items: center;
    font-size: 15.5px;
    line-height: 27px;
  }
  .contact__icon {
    width: 13px;
    height: 13px;
    margin-right: 16px;
    fill: var(--ink-gray);
  }
</style>
</head>
<body>
<main class="canvas">

  <section class="card card--back" aria-label="Card back">
    <div class="brand">
      <span class="brand__mark"></span>
      <span class="brand__name">Silverpine</span>
      <span class="brand__sub">Strategies</span>
    </div>
    <p class="address">718 B North Larkmoor Avenue, NE<br>Washington, DC 20019</p>
    <p class="services">Fundraising<span class="services__sep">|</span>Event Planning<span class="services__sep">|</span>Political Consulting</p>
  </section>

  <section class="card card--front" aria-label="Card front">
    <div class="brand">
      <span class="brand__mark"></span>
      <span class="brand__name">Silverpine</span>
      <span class="brand__sub">Strategies</span>
    </div>
    <div class="card__panel">
      <p class="person__name">Carla Merrow</p>
      <p class="person__title">Partner</p>
      <ul class="contact">
        <li class="contact__item">
          <svg class="contact__icon" viewBox="0 0 16 16" aria-hidden="true"><path d="M1 5c0-2 3-3 7-3s7 1 7 3v1h-3V4.5C11 4 10 4 8 4s-3 0-4 .5V6H1z"/><path d="M4 7h8l2 6H2z"/></svg>
          202.555.0147
        </li>
        <li class="contact__item">
          <svg class="contact__icon" viewBox="0 0 16 16" aria-hidden="true"><path d="M4 0h8a1 1 0 0 1 1 1v14a1 1 0 0 1-1 1H4a1 1 0 0 1-1-1V1a1 1 0 0 1 1-1zm1 2v10h6V2zm3 11a1 1 0 1 0 0 2 1 1 0 0 0 0-2z"/></svg>
          202.555.0183
        </li>
        <li class="contact__item">
          <svg class="contact__icon" viewBox="0 0 16 16" aria-hidden="true"><path d="M0 3h16v1L8 9 0 4z"/><path d="M0 5.5l8 5 8-5V13H0z"/></svg>
          carla@silverpinellc.com
        </li>
        <li class="contact__item">
          <svg class="contact__icon" viewBox="0 0 16 16" aria-hidden="true"><circle cx="8" cy="8" r="7" fill="none" stroke="#6a6a6a" stroke-width="1.6"/><path d="M1 8h14M8 1c-3 3.5-3 10.5 0 14M8 1c3 3.5 3 10.5 0 14" fill="none" stroke="#6a6a6a" stroke-width="1.2"/></svg>
          www.silverpinellc.com
        </li>
      </ul>
    </div>
  </section>

</main>
</body>
</html>
```